Brookvale Rendering Wordpress Design

I would like a design for my friends company. He has just had his logo designed and really likes the following website.

www.tlb-rendering.co.uk

Something similar to this design would be ideal but open to additional ideas. The website shown has all the relevant content.

We have 20 years of experience and can provide a number of photos for work we have done.

More photos will be provided upon request.

Target Market(s)

Homeowners

Industry/Entity Type

Trade

Font styles to use
Sans Serif

Colors
3176b5
85cae6
85abd2
eaf1f7

Requirements
Must have
• look at www.tlb-rendering.co.uk
Nice to have
Should not have
• N/A

```html
<!DOCTYPE html>
<html lang="en">
<head>
<meta charset="utf-8">
<title>Brookvale Rendering – Home</title>
<link rel="stylesheet" href="https://fonts.googleapis.com/css2?family=Open+Sans:wght@400;600;700;800&display=swap">
<style>
:root{
  --brand:#31679f;
  --brand-dark:#2b5d91;
  --accent:#85cae6;
  --ink:#222;
  --muted:#555;
  --rule:#3176b5;
  --soft:#eff0f1;
  --white:#fff;
}
*{box-sizing:border-box;margin:0;padding:0}
html,body{width:1200px;height:1200px;overflow:hidden;background:#fff}
body{font-family:"Open Sans",Arial,sans-serif;color:var(--ink)}
.page{width:1200px;height:1200px;position:relative;overflow:hidden}

.topbar{height:36px;background:var(--brand);color:#fff;font-size:12px;display:flex;align-items:center;padding:0 160px}
.topbar .contact{display:flex;gap:22px;align-items:center}
.topbar .contact span{display:flex;align-items:center;gap:7px}
.topbar .social{margin-left:auto;display:flex;height:36px}
.topbar .social i{width:30px;border-left:1px solid rgba(255,255,255,.25);display:flex;align-items:center;justify-content:center}
.topbar .social i:last-child{border-right:1px solid rgba(255,255,255,.25)}
.topbar .social i::after{content:"";width:9px;height:9px;background:rgba(255,255,255,.85);border-radius:2px}

.header{height:74px;display:flex;align-items:center;padding:0 160px;border-bottom:1px solid #eee}
.brand{display:flex;align-items:center;gap:10px;font-weight:600;font-size:19px;color:var(--brand);letter-spacing:.5px}
.brand .mark{width:14px;height:14px;background:var(--brand)}
.nav{margin-left:auto;display:flex;gap:26px;font-size:11px;font-weight:600;color:#333;letter-spacing:.3px}
.nav .active{color:var(--rule)}

.hero{height:340px;position:relative;background:linear-gradient(100deg,#dfe0e1 0%,#c9cdd2 35%,#e6e7e8 60%,#d8dadb 100%)}
.hero .welcome{position:absolute;left:760px;top:70px;width:330px;height:220px;background:var(--brand);color:#fff;padding:18px 26px}
.welcome h1{font-size:27px;font-weight:700;line-height:1.17;letter-spacing:.5px}
.welcome p{font-size:13px;line-height:1.45;margin-top:9px;color:#e3ecf5}
.welcome .btn{display:inline-block;margin-top:16px;background:var(--accent);color:var(--brand-dark);font-weight:700;font-size:12.5px;padding:6px 12px;letter-spacing:.4px}

.section{text-align:center}
.section h2{font-size:19px;font-weight:600;letter-spacing:.6px}
.section h2::after{content:"";display:block;width:80px;height:2px;background:var(--rule);margin:9px auto 0}
.section .lead{font-size:13px;color:#333;margin-top:14px}

.services{padding-top:34px;height:420px}
.cards{display:flex;width:810px;margin:26px auto 0}
.card{width:270px}
.card .photo{height:160px}
.card h3{font-size:12px;font-weight:600;letter-spacing:.4px;margin-top:16px}
.card h3::after{content:"";display:block;width:70px;height:2px;background:var(--rule);margin:8px auto 0}
.card p{font-size:10.2px;line-height:1.45;color:var(--muted);margin-top:12px;padding:0 6px}

.about{background:var(--soft);padding-top:32px;height:330px}
.about .row{display:flex;width:810px;margin:24px auto 0;gap:14px;text-align:left}
.about .video{width:400px;height:190px;flex:none;background:linear-gradient(180deg,#6f6a63,#a9a49c 55%,#8f8a82);position:relative}
.about .video svg{position:absolute;left:180px;top:75px}
.about .copy p{font-size:10.2px;line-height:1.45;color:#555;margin-bottom:12px}
</style>
</head>
<body>
<div class="page">
  <div class="topbar">
    <div class="contact">
      <span><svg width="11" height="11" viewBox="0 0 24 24" fill="#fff"><path d="M6.6 10.8a15 15 0 0 0 6.6 6.6l2.2-2.2c.3-.3.7-.4 1-.2 1.1.4 2.3.6 3.6.6.6 0 1 .4 1 1V20c0 .6-.4 1-1 1A17 17 0 0 1 3 4c0-.6.4-1 1-1h3.5c.6 0 1 .4 1 1 0 1.3.2 2.5.6 3.6.1.3 0 .7-.2 1z"/></svg>0555-018-2240</span>
      <span><svg width="12" height="10" viewBox="0 0 24 18" fill="none" stroke="#fff" stroke-width="2"><rect x="1" y="1" width="22" height="16"/><path d="M1 1l11 9 11-9"/></svg>info@brookvalerendering.com</span>
    </div>
    <div class="social"><i></i><i></i><i></i><i></i></div>
  </div>

  <header class="header">
    <div class="brand"><span class="mark"></span>Brookvale Rendering</div>
    <nav class="nav">
      <span>HOME</span><span class="active">SERVICES</span><span>PRODUCTS</span><span>FREE ESTIMATE</span><span>TESTIMONIALS</span><span>BLOG</span><span>CONTACT</span>
    </nav>
  </header>

  <section class="hero" role="img" aria-label="Two plasterers in hard hats and blue overalls working on a white wall">
    <div class="welcome">
      <h1>WELCOME TO<br>OUR COMPANY</h1>
      <p>There are many variations of passages of Lorem Ipsum available, but the majority have suffered alteration in some form</p>
      <span class="btn">ENQUIRE NOW</span>
    </div>
  </section>

  <section class="section services">
    <h2>OUR COMPANY SERVICES</h2>
    <p class="lead">The following are the services which we are pleased to offer</p>
    <div class="cards">
      <div class="card">
        <div class="photo" role="img" aria-label="Stone house with a rendered facade" style="background:linear-gradient(180deg,#8fb3d9 0%,#7b6a5c 45%,#5e5249 100%)"></div>
        <h3>RENDERING</h3>
        <p>Our team of experienced plasterers provide a full range of rendering services in Plymouth. From Sand &amp; cement rendering to through colour and thin coat renders. Contact us for a no obligation quote.</p>
      </div>
      <div class="card">
        <div class="photo" role="img" aria-label="Worker smoothing plaster on a wall with a trowel" style="background:linear-gradient(110deg,#d9dcdf 0%,#b9bec4 50%,#c99a4a 85%)"></div>
        <h3>PLASTERBOARD / DRY LINING</h3>
        <p>We can undertake all aspects of dry lining from large scale housing contracts to simply over boarding a ceiling. If you need a plasterer in Plymouth, for a competitive, no obligation quote please contact us.</p>
      </div>
      <div class="card">
        <div class="photo" role="img" aria-label="Worker fitting insulation panels to an external wall" style="background:linear-gradient(110deg,#6e6e6e 0%,#c23a4a 40%,#9a8a6c 70%,#3d3d42 100%)"></div>
        <h3>EXTERNAL WALL INSULATION</h3>
        <p>Solid walls can be insulated from the outside where a layer of insulation material is fixed to your property's external walls. Then a protective layers of render or cladding applied, designed to suit you and your home's style.</p>
      </div>
    </div>
  </section>

  <section class="section about">
    <h2>ABOUT OUR COMPANY</h2>
    <p class="lead">Harbourline Heat Treatment is a preferred solution over Chemicals?</p>
    <div class="row">
      <div class="video" role="img" aria-label="Video still of a room under renovation">
        <svg width="40" height="40" viewBox="0 0 40 40"><circle cx="20" cy="20" r="19" fill="rgba(255,255,255,.85)" stroke="#31679f" stroke-width="2"/><path d="M16 12l11 8-11 8z" fill="#31679f"/></svg>
      </div>
      <div class="copy">
        <p>There are many variations of passages of Lorem Ipsum available, but the majority have suffered alteration in some form, by injected humour, or randomised words which don't look even slightly believable. If you are going to use a passage of Lorem Ipsum.</p>
        <p>There are many variations of passages of Lorem Ipsum available, but the majority have suffered alteration in some form, by injected humour, or randomised words which don't look even slightly believable. If you are going to use a passage of Lorem Ipsum.</p>
      </div>
    </div>
  </section>
</div>
</body>
</html>
```